New Company Business Card design

Looking for a corporate looking business card utilising my new logo design - the logo i would like embossed as one option and flat as another - simplistic but stylish - less is more - we are an import export business launching into the market - i would like a couple of options as main background - Grey or Black

```html
<!DOCTYPE html>
<html lang="en">
<head>
<meta charset="utf-8">
<title>Meridian Trade Partners – Business Card</title>
<link rel="stylesheet" href="https://fonts.googleapis.com/css2?family=Roboto:wght@400;500;700&display=swap">
<style>
  :root {
    --backdrop: #e6e1da;
    --card: #3a3d42;
    --brand-blue: #4aa3e0;
    --ink-light: #e3e5e8;
    --soft-grey: #9a9ea4;
  }
  * { box-sizing: border-box; margin: 0; padding: 0; }
  html, body { width: 1200px; height: 848px; overflow: hidden; }
  body {
    background: var(--backdrop);
    font-family: "Roboto", Arial, sans-serif;
    position: relative;
  }
  .card {
    position: absolute;
    left: 300px;
    width: 600px;
    height: 343px;
    background: var(--card);
    box-shadow: 0 6px 18px rgba(0,0,0,0.18);
  }
  .card--front { top: 60px; }
  .card--back { top: 445px; }

  .front-brand {
    position: absolute;
    inset: 0;
    display: flex;
    flex-direction: column;
    align-items: center;
    justify-content: center;
    gap: 12px;
    padding-bottom: 20px;
  }
  .brand-row { display: flex; align-items: center; gap: 14px; }
  .brand-dot {
    width: 22px; height: 22px; border-radius: 50%;
    background: var(--brand-blue);
    flex: none;
  }
  .brand-name {
    color: var(--brand-blue);
    font-weight: 700;
    font-size: 32px;
    letter-spacing: 1px;
    text-transform: uppercase;
    white-space: nowrap;
  }
  .brand-rule { width: 420px; height: 2px; background: var(--soft-grey); }
  .tagline {
    color: var(--ink-light);
    font-size: 13px;
    font-weight: 500;
    letter-spacing: 3px;
    text-transform: uppercase;
    white-space: nowrap;
  }

  .back-brand {
    position: absolute;
    left: 44px; top: 70px;
    display: flex; align-items: center; gap: 10px;
  }
  .back-brand .brand-dot { width: 16px; height: 16px; }
  .back-brand .brand-name { font-size: 19px; line-height: 1.25; letter-spacing: 0.5px; }

  .contact {
    position: absolute;
    right: 34px; top: 68px;
    text-align: right;
    color: var(--ink-light);
    font-size: 13.5px;
    line-height: 1.4;
  }
  .contact__name { color: var(--brand-blue); font-weight: 700; font-size: 19px; line-height: 1.2; }
  .contact__role { font-size: 13.5px; margin-bottom: 14px; }
  .contact__address { margin-bottom: 10px; }
  .contact__line { display: flex; justify-content: flex-end; align-items: center; gap: 8px; white-space: nowrap; }
  .contact__line svg { width: 13px; height: 13px; fill: var(--brand-blue); flex: none; }
</style>
</head>
<body>

<section class="card card--front" aria-label="Card front">
  <div class="front-brand">
    <div class="brand-row">
      <span class="brand-dot"></span>
      <span class="brand-name">Meridian Trade Partners</span>
    </div>
    <div class="brand-rule"></div>
    <p class="tagline">Worldwide Supply for Everyday Needs</p>
  </div>
</section>

<section class="card card--back" aria-label="Card back">
  <div class="back-brand">
    <span class="brand-dot"></span>
    <span class="brand-name">Meridian<br>Trade Partners</span>
  </div>

  <div class="contact">
    <p class="contact__name">DANIEL HARTLEY</p>
    <p class="contact__role">CEO/FOUNDER</p>
    <p class="contact__address">214 Harbour View Road<br>Portside, Nova 50321</p>
    <p class="contact__line">555 210 4471
      <svg viewBox="0 0 16 16" aria-hidden="true"><path d="M3 1l3 3-1.5 2a9 9 0 0 0 5.5 5.5L12 10l3 3-2 2C7 15 1 9 1 3z"/></svg></p>
    <p class="contact__line">555 318 2290
      <svg viewBox="0 0 16 16" aria-hidden="true"><path d="M4 0h8v16H4zM5.5 2v10h5V2zM7 13.5h2v1H7z" fill-rule="evenodd"/></svg></p>
    <p class="contact__line">555 604 7735
      <svg viewBox="0 0 16 16" aria-hidden="true"><path d="M4 1h7v4H4zM1 6h14v7h-3v3H4v-3H1zM5 11v3h6v-3z" fill-rule="evenodd"/></svg></p>
    <p class="contact__line">hello@meridiantrade.example
      <svg viewBox="0 0 16 16" aria-hidden="true"><path d="M1 3h14v10H1zM2.5 4.5L8 9l5.5-4.5z" fill-rule="evenodd"/></svg></p>
    <p class="contact__line">www.meridiantrade.example
      <svg viewBox="0 0 16 16" aria-hidden="true"><circle cx="8" cy="8" r="7"/></svg></p>
  </div>
</section>

</body>
</html>
```